Start up Dialysis Clinic needs its first website - Torvane Health

Create a visually appealing and user-friendly website for Torvane Health, a dialysis clinic located in Mt. Irvine, Tobago. The website should effectively communicate our services to local, regional, and international patients, providing essential information and fostering trust and engagement..
Key Goals:

1. Informative: Provide comprehensive information about our services, facility, and team.
2. User-Friendly: Ensure the website is easy to navigate, with a clear structure and accessible content.
3. Engaging: Create a visually appealing design that reflects the professionalism and care of Torvane Health.
4. Responsive: Ensure the website is fully responsive and performs well on all devices, including desktops, tablets, and smartphones.
5. Trust-Building: Include testimonials, credentials, and patient resources to build trust with potential patients.
Scope of Work:

1. Home Page: An inviting and informative landing page that provides an overview of our clinic, mission, and services. Include a call to action for more information and contact details.
2. About Us: A detailed page about Torvane Health, including our mission, vision, team, and facility tour.
3. Services: A comprehensive page describing the dialysis services we offer, including Hemodialysis, Peritoneal Dialysis, and Home Hemodialysis.
4. Patient Information: A resourceful section with guides for new patients, FAQs, insurance and billing information, and downloadable forms.
5. Resources: Educational content about kidney health, dialysis options, diet and nutrition tips, and support groups.
6. Contact Us: A contact page with our address, phone number, email, office hours, a contact form, and a map.

```html
<!DOCTYPE html>
<html lang="en">
<head>
<meta charset="utf-8">
<title>Torvane Health – Dialysis Clinic</title>
<link href="https://fonts.googleapis.com/css2?family=Open+Sans:wght@400;600;700&display=swap" rel="stylesheet">
<style>
:root{
  --navy:#13204a;
  --navy-deep:#0f1a3d;
  --navy-bar:#1b2752;
  --blue:#3b6db3;
  --green:#4a8f2c;
  --orange:#f0a33c;
  --text:#333;
  --muted:#8a8f99;
  --white:#fff;
}
*{margin:0;padding:0;box-sizing:border-box}
html,body{width:1200px;height:4881px;overflow:hidden}
body{font-family:"Open Sans",Arial,sans-serif;color:var(--text);background:var(--white)}
.page{position:relative;width:1200px;height:4881px;overflow:hidden}
.abs{position:absolute}
.photo{position:absolute}
a{color:inherit;text-decoration:none}

.topbar{left:390px;top:0;width:810px;height:32px;background:var(--navy);color:#fff;font-size:11px;font-weight:600;display:flex;align-items:center}
.topbar .item{display:flex;align-items:center;gap:8px;height:32px}
.topbar .phone{width:203px;justify-content:center}
.topbar .appt{width:232px;background:var(--green);justify-content:center}
.topbar .addr{padding-left:38px}
.logo{display:flex;align-items:center;gap:8px;color:var(--blue);font-weight:700;font-size:20px}
.logo .mark{width:22px;height:22px;background:var(--green)}
.nav{left:396px;top:60px;display:flex;gap:38px;font-size:11px;font-weight:600;color:#333}
.btn-outline{left:931px;top:53px;width:117px;height:32px;border:1.5px solid var(--orange);border-radius:3px;color:var(--orange);font-size:10px;font-weight:600;display:flex;align-items:center;justify-content:center}

.hero{left:0;top:102px;width:1200px;height:694px;background:linear-gradient(120deg,#3c4147,#22272c 55%,#1a1e22)}
.eyebrow-line{display:flex;align-items:center;gap:16px;justify-content:center;color:#fff;font-size:12px}
.eyebrow-line span.bar{width:36px;height:2px;background:var(--green)}
.hero-title{left:0;width:1200px;top:344px;text-align:center;color:#fff;font-size:50px;font-weight:700;line-height:60px}
.btn-green{background:var(--green);color:#fff;font-weight:600;font-size:13px;display:flex;align-items:center;justify-content:center;gap:10px;border-radius:2px}

.kicker{color:var(--green);font-size:11px;font-weight:600;text-decoration:underline;text-underline-offset:3px}
.h2{font-weight:700;color:var(--navy);font-size:37px;line-height:46px}
.h2 .accent{color:var(--blue)}
.para{font-size:11.5px;line-height:19px;color:var(--muted)}

.services{left:0;top:1509px;width:1200px;height:789px;background:linear-gradient(180deg,#2a2c30,#1f2124)}
.card-img{width:283px;height:279px}
.icon-box{width:76px;height:76px;background:#fff;display:flex;align-items:center;justify-content:center}
.card-title{color:#fff;font-size:16px;font-weight:700;text-align:center}
.card-text{color:#dcdcdc;font-size:12.5px;line-height:21px;text-align:center}

.faq-q{font-size:14.5px;font-weight:700;color:var(--navy)}
.faq-toggle{width:48px;height:48px;border-radius:50%;background:var(--navy);color:#fff;display:flex;align-items:center;justify-content:center;font-size:20px}
.faq-toggle.open{background:var(--green)}
.faq-line{height:1px;background:#b9bcc3;width:509px;left:536px}

.journey{left:0;top:2967px;width:1200px;height:796px}
.feat-title{color:#fff;font-size:15px;font-weight:700}
.feat-text{color:#cfcfcf;font-size:11.5px;line-height:19px}

.quote-box{left:131px;top:3915px;width:940px;height:203px;border:1px solid #cfd2d8}
.avatar{border-radius:50%}
.stars{color:#f2b632;font-size:20px;letter-spacing:2px}

.footer{left:0;top:4285px;width:1200px;height:540px;background:var(--navy-deep)}
.social{width:38px;height:38px;border-radius:3px}
.bottom-bar{left:0;top:4825px;width:1200px;height:56px;background:var(--navy-bar);color:#fff;font-size:12px}
.contact-item{display:flex;align-items:center;gap:16px;color:#fff}
.contact-item .lbl{font-size:14px;color:#c7cbd6}
.contact-item .val{font-size:15px;font-weight:700;white-space:nowrap}
</style>
</head>
<body>
<div class="page">

<header>
  <div class="abs logo" style="left:91px;top:34px"><span class="mark"></span>Torvane Health</div>
  <div class="abs topbar">
    <div class="item phone">
      <svg width="14" height="14" viewBox="0 0 24 24" fill="none" stroke="#fff" stroke-width="2"><path d="M22 16.9v3a2 2 0 0 1-2.2 2 19.8 19.8 0 0 1-8.6-3.1 19.5 19.5 0 0 1-6-6A19.8 19.8 0 0 1 2.1 4.2 2 2 0 0 1 4.1 2h3a2 2 0 0 1 2 1.7c.1.9.4 1.8.7 2.7a2 2 0 0 1-.5 2.1L8 9.8a16 16 0 0 0 6 6l1.3-1.3a2 2 0 0 1 2.1-.4c.9.3 1.8.6 2.7.7a2 2 0 0 1 1.7 2z"/></svg>
      868 - 555 - 0142</div>
    <div class="item appt">
      <svg width="13" height="13" viewBox="0 0 24 24" fill="none" stroke="#fff" stroke-width="2"><rect x="3" y="4" width="18" height="18" rx="2"/><path d="M16 2v4M8 2v4M3 10h18"/></svg>
      REQUEST AN APPOINTMENT</div>
    <div class="item addr">
      <svg width="12" height="14" viewBox="0 0 24 24" fill="none" stroke="#fff" stroke-width="2"><path d="M12 22s-8-6.5-8-13a8 8 0 0 1 16 0c0 6.5-8 13-8 13z"/><circle cx="12" cy="9" r="3"/></svg>
      18 Shore Road, Mt. Irvine</div>
  </div>
  <nav class="abs nav"><a>Home</a><a>Services</a><a>About Us</a><a>Resources</a><a>FAQs</a></nav>
  <a class="abs btn-outline">CONTACT US</a>
</header>

<section>
  <div class="photo hero" role="img" aria-label="Photo of medical staff walking through a hospital corridor, darkened"></div>
  <div class="abs eyebrow-line" style="left:0;width:1200px;top:313px"><span class="bar"></span>WE ARE THE BEST IN TOWN<span class="bar"></span></div>
  <h1 class="abs hero-title">Empower your Body,<br>Empower your Life.</h1>
  <p class="abs" style="left:0;width:1200px;top:487px;text-align:center;color:#fff;font-size:14px;font-weight:600">Top Rated Dialysis Experts in the City</p>
  <a class="abs btn-green" style="left:508px;top:538px;width:159px;height:42px">More Details</a>
  <svg class="abs" style="left:0;top:716px" width="1200" height="82" viewBox="0 0 1200 82">
    <path d="M0,82 V50 Q600,-16 1200,50 V82Z" fill="#fff"/>
  </svg>
</section>

<section>
  <div class="abs" style="left:78px;top:1003px;width:150px;height:190px;border-radius:50%;background:#d4f0fb"></div>
  <div class="photo" style="left:201px;top:908px;width:364px;height:431px;border-radius:0 24px 24px 24px;background:linear-gradient(135deg,#3f5e7a,#c9d6df 60%,#eef1f4)" role="img" aria-label="Photo of a doctor in a white coat holding a stethoscope"></div>
  <div class="abs" style="left:125px;top:1105px;width:345px;height:345px;border-radius:28px;background:#fff;box-shadow:0 4px 14px rgba(0,0,0,.12)"></div>
  <div class="photo" style="left:139px;top:1119px;width:317px;height:317px;border-radius:22px;background:linear-gradient(160deg,#a9a7a0,#5a4a44 55%,#2e2a2e)" role="img" aria-label="Photo of a smiling doctor holding a clipboard in a clinic"></div>

  <div class="abs kicker" style="left:618px;top:977px">WHO WE ARE</div>
  <h2 class="abs h2" style="left:618px;top:1008px;width:480px">Your Partner in <span class="accent">Kidney Wellness</span></h2>
  <p class="abs" style="left:618px;top:1127px;font-size:17px;color:#222">Transform your body, transform your life.</p>
  <p class="abs para" style="left:618px;top:1162px;width:455px">Lorem ipsum dolor sit amet, consectetur adipiscing elit, sed do eiusmod tempor incididunt ut labore et dolore magna aliqua. Ut enim ad minim veniam, quis laboris nisi ut aliquip ex ea commodo consequat.</p>
  <p class="abs para" style="left:618px;top:1231px;width:455px">Lorem ipsum dolor sit amet, consectetur adipiscing elit, sed do eiusmod tempor incididunt ut labore et dolore magna aliqua.</p>
  <a class="abs btn-green" style="left:618px;top:1299px;width:137px;height:40px">Contact us
    <svg width="16" height="12" viewBox="0 0 16 12" fill="none" stroke="#fff" stroke-width="1.6"><path d="M1 6h13M9 1l5 5-5 5"/></svg></a>
</section>

<section>
  <div class="photo services" role="img" aria-label="Darkened photo of a clinical team at work"></div>
  <svg class="abs" style="left:0;top:1508px" width="1200" height="80" viewBox="0 0 1200 80">
    <path d="M0,0 H1200 V10 Q600,84 0,10Z" fill="#fff"/>
  </svg>
  <div class="abs" style="left:0;width:1200px;top:1645px;text-align:center;color:#fff;font-size:12px;text-decoration:underline;text-underline-offset:3px">OUR SERVICES</div>
  <h2 class="abs" style="left:0;width:1200px;top:1682px;text-align:center;color:#fff;font-size:40px;font-weight:700">Services We Provide</h2>

  <div class="abs" style="left:775px;top:2057px;width:371px;height:28px;background:#2e3034"></div>

  <div class="photo card-img" style="left:119px;top:1778px;background:linear-gradient(135deg,#d9d4d2,#b8423f 55%,#e8e6e6)" role="img" aria-label="Photo of a patient's arm connected to dialysis tubing"></div>
  <div class="abs icon-box" style="left:349px;top:1800px">
    <svg width="36" height="36" viewBox="0 0 36 36" fill="none" stroke="#4a8f2c" stroke-width="2"><circle cx="18" cy="10" r="4"/><path d="M8 30h22M12 30l6-14 6 8M22 24l4 6"/></svg></div>
  <h3 class="abs card-title" style="left:119px;top:2078px;width:283px">Hemodialysis</h3>
  <p class="abs card-text" style="left:119px;top:2112px;width:283px">Lorem ipsum dolor sit amet, consectetur adipiscing elit, sed do ei</p>

  <div class="photo card-img" style="left:447px;top:1778px;background:linear-gradient(135deg,#e9ecef,#9aa4ad 60%,#3e4650)" role="img" aria-label="Photo of a doctor holding a magnifying glass over a kidney model"></div>
  <div class="abs icon-box" style="left:677px;top:1800px">
    <svg width="36" height="36" viewBox="0 0 36 36" fill="none" stroke="#4a8f2c" stroke-width="2"><circle cx="18" cy="20" r="12"/><path d="M18 20l5-6M10 20h2M24 20h2M18 12v2"/></svg></div>
  <h3 class="abs card-title" style="left:447px;top:2078px;width:283px">Peritoneal Dialysis</h3>
  <p class="abs card-text" style="left:447px;top:2112px;width:283px">Lorem ipsum dolor sit amet, consectetur adipiscing elit, sed do ei</p>

  <div class="photo card-img" style="left:775px;top:1778px;background:linear-gradient(135deg,#4e6a9e,#8ea3c9 55%,#c94a4a)" role="img" aria-label="Photo of a bandaged arm with a dialysis line at home"></div>
  <div class="abs icon-box" style="left:1005px;top:1800px">
    <svg width="36" height="36" viewBox="0 0 36 36" fill="none" stroke="#4a8f2c" stroke-width="2"><path d="M18 5l12 9-4 15H10L6 14z"/><circle cx="18" cy="18" r="3"/></svg></div>
  <h3 class="abs card-title" style="left:775px;top:2078px;width:283px">Home Hemodialysis</h3>
  <p class="abs card-text" style="left:775px;top:2112px;width:283px">Lorem ipsum dolor sit amet, consectetur adipiscing elit, sed do ei</p>

  <svg class="abs" style="left:0;top:2218px" width="1200" height="82" viewBox="0 0 1200 82">
    <path d="M0,82 V50 Q600,-16 1200,50 V82Z" fill="#fff"/>
  </svg>
</section>

<section>
  <div class="abs" style="left:156px;top:2390px;width:11px;height:11px;background:var(--green)"></div>
  <div class="abs" style="left:181px;top:2386px;font-size:13px;font-weight:700;color:var(--navy)">FAQ</div>
  <h2 class="abs" style="left:154px;top:2422px;font-size:35px;font-weight:700;line-height:49px;color:var(--navy)">FREQUENTLY<br>ASKED QUESTIONS</h2>
  <div class="photo" style="left:154px;top:2544px;width:324px;height:323px;border-radius:14px;background:linear-gradient(160deg,#e7eaee,#b9b0a7 50%,#4d6a8f)" role="img" aria-label="Photo of a smiling doctor seated at a desk with dental models"></div>

  <div class="abs faq-q" style="left:536px;top:2417px">How do I get consultations started?</div>
  <div class="abs faq-toggle" style="left:994px;top:2402px">+</div>
  <div class="abs faq-line" style="top:2477px"></div>

  <div class="abs faq-q" style="left:536px;top:2513px">How do I get consultations started?</div>
  <div class="abs faq-toggle open" style="left:994px;top:2498px">–</div>
  <p class="abs" style="left:536px;top:2550px;width:470px;font-size:14px;line-height:26px;color:#6b6f78">Lorem ipsum dolor sit amet, consectetur adipiscing elit, sed do eiusmod tempor incididunt ut labore et dolore magna aliqua. Ut enim ad minim veniam, Lorem ipsum dolor sit amet consectetur</p>
  <div class="abs faq-line" style="top:2677px"></div>

  <div class="abs faq-q" style="left:536px;top:2714px">How do I get consultations started?</div>
  <div class="abs faq-toggle" style="left:994px;top:2700px">+</div>
  <div class="abs faq-line" style="top:2772px"></div>

  <div class="abs faq-q" style="left:536px;top:2811px">How do I get consultations started?</div>
  <div class="abs faq-toggle" style="left:994px;top:2797px">+</div>
  <div class="abs faq-line" style="top:2869px"></div>
</section>

<section>
  <div class="photo journey" style="background:linear-gradient(90deg,#2d2f32 45%,#3a3d42 70%,#2b2d30)" role="img" aria-label="Darkened photo of a senior doctor and a colleague reviewing a tablet"></div>
  <svg class="abs" style="left:0;top:2966px" width="1200" height="80" viewBox="0 0 1200 80">
    <path d="M0,0 H1200 V10 Q600,84 0,10Z" fill="#fff"/>
  </svg>
  <div class="abs kicker" style="left:129px;top:3148px">WHO WE ARE</div>
  <h2 class="abs" style="left:129px;top:3178px;color:#fff;font-size:37px;font-weight:700;line-height:46px">Embrace the journey,<br>see the results</h2>
  <p class="abs" style="left:129px;top:3290px;width:455px;color:#e3e3e3;font-size:11.5px;line-height:19px">Lorem ipsum dolor sit amet, consectetur adipiscing elit, sed do eiusmod tempor or incididunt ut labore et dolore magna aliqua. Ut enim ad minim veniam, quis laboris nisi ut aliquip ex ea commodo consequat.</p>

  <svg class="abs" style="left:129px;top:3376px" width="32" height="32" viewBox="0 0 32 32" fill="none" stroke="#fff" stroke-width="2.4"><rect x="2" y="4" width="24" height="24"/><path d="M8 16l6 6L30 4"/></svg>
  <div class="abs feat-title" style="left:181px;top:3372px">Professional</div>
  <div class="abs feat-text" style="left:181px;top:3396px;width:150px">Inventore veritasis uas vitae dicta sunt</div>
  <svg class="abs" style="left:337px;top:3376px" width="32" height="32" viewBox="0 0 32 32" fill="none" stroke="#fff" stroke-width="2.4"><rect x="2" y="4" width="24" height="24"/><path d="M8 16l6 6L30 4"/></svg>
  <div class="abs feat-title" style="left:389px;top:3372px">Empathetic</div>
  <div class="abs feat-text" style="left:389px;top:3396px;width:150px">Inventore veritasis uas vitae dicta sunt</div>
  <svg class="abs" style="left:129px;top:3465px" width="32" height="32" viewBox="0 0 32 32" fill="none" stroke="#fff" stroke-width="2.4"><rect x="2" y="4" width="24" height="24"/><path d="M8 16l6 6L30 4"/></svg>
  <div class="abs feat-title" style="left:181px;top:3460px">Confidential</div>
  <div class="abs feat-text" style="left:181px;top:3484px;width:150px">Inventore veritasis uas vitae dicta sunt</div>
  <svg class="abs" style="left:337px;top:3465px" width="32" height="32" viewBox="0 0 32 32" fill="none" stroke="#fff" stroke-width="2.4"><rect x="2" y="4" width="24" height="24"/><path d="M8 16l6 6L30 4"/></svg>
  <div class="abs feat-title" style="left:389px;top:3460px">Expertise</div>
  <div class="abs feat-text" style="left:389px;top:3484px;width:150px">Inventore veritasis uas vitae dicta sunt</div>

  <a class="abs btn-green" style="left:129px;top:3562px;width:138px;height:38px">Contact us
    <svg width="16" height="12" viewBox="0 0 16 12" fill="none" stroke="#fff" stroke-width="1.6"><path d="M1 6h13M9 1l5 5-5 5"/></svg></a>

  <svg class="abs" style="left:0;top:3683px" width="1200" height="82" viewBox="0 0 1200 82">
    <path d="M0,82 V50 Q600,-16 1200,50 V82Z" fill="#fff"/>
  </svg>
</section>

<section>
  <div class="abs" style="left:0;width:1200px;top:3786px;text-align:center;color:var(--green);font-size:12px;text-decoration:underline;text-underline-offset:3px">TESTIMONIALS</div>
  <h2 class="abs" style="left:0;width:1200px;top:3822px;text-align:center;font-size:40px;font-weight:600;color:var(--navy)"><span style="color:var(--blue)">Clients</span> Love Us</h2>
  <div class="abs quote-box"></div>
  <div class="abs" style="left:175px;top:3990px;font-size:160px;line-height:1;color:#eeeff2;font-weight:700">”</div>
  <p class="abs" style="left:175px;top:3955px;width:850px;text-align:center;font-size:11.5px;line-height:19px;color:#6f737c">Lorem ipsum dolor sit amet, consectetur adipiscing elit, sed do eiusmod tempor incididunt ut labore et dolore magna aliqua. Ut enim ad minim veniam, quis nostrud exercitation ullamco laboris nisi ut aliquip ex ea commodo consequat. Duis aute irure dolor in reprehenderit in Lorem ipsum do r sit amet, consectetur adipiscing elit, sed do eiusmod tempor incididunt ut labore et dolore Lorem ipsum dolor sit amet, consectetur a dipiscing elit, sed do eiusmod tempor incididunt ut labore et dolore</p>
  <div class="photo avatar" style="left:429px;top:4084px;width:86px;height:86px;background:linear-gradient(#b9b5b0,#55504c)" role="img" aria-label="Client portrait"></div>
  <div class="abs avatar" style="left:537px;top:4063px;width:128px;height:128px;border:4px solid var(--blue);background:#fff"></div>
  <div class="photo avatar" style="left:546px;top:4072px;width:110px;height:110px;background:linear-gradient(#3c6aa8,#d6c2a8 60%,#2d3d5a)" role="img" aria-label="Client portrait"></div>
  <div class="photo avatar" style="left:685px;top:4084px;width:86px;height:86px;background:linear-gradient(#cfcac4,#5a4236)" role="img" aria-label="Client portrait"></div>
  <svg class="abs" style="left:482px;top:4212px" width="28" height="14" viewBox="0 0 28 14" fill="none" stroke="#222" stroke-width="1.6"><path d="M27 7H2M8 1L2 7l6 6"/></svg>
  <div class="abs" style="left:0;width:1200px;top:4208px;text-align:center;font-size:17px;color:var(--blue)">Daniel Ashby</div>
  <svg class="abs" style="left:692px;top:4212px" width="28" height="14" viewBox="0 0 28 14" fill="none" stroke="#222" stroke-width="1.6"><path d="M1 7h25M20 1l6 6-6 6"/></svg>
  <div class="abs stars" style="left:0;width:1200px;top:4236px;text-align:center">★★★★★</div>
</section>

<footer>
  <div class="abs footer"></div>
  <svg class="abs" style="left:0;top:4284px" width="1200" height="80" viewBox="0 0 1200 80">
    <path d="M0,0 H1200 V10 Q600,84 0,10Z" fill="#fff"/>
  </svg>
  <div class="abs social" style="left:84px;top:4423px;background:#3b5a9a"></div>
  <div class="abs social" style="left:134px;top:4423px;background:#1f6fb3"></div>
  <div class="abs social" style="left:184px;top:4423px;background:#2aa3e8"></div>
  <div class="abs social" style="left:234px;top:4423px;background:#e0243a"></div>
  <div class="abs logo" style="left:0;width:1200px;top:4428px;justify-content:center"><span class="mark"></span>Torvane Health</div>
  <div class="abs" style="left:969px;top:4431px;color:#fff;font-size:14px;font-weight:700">Back to top</div>
  <div class="abs" style="left:1070px;top:4420px;width:42px;height:42px;background:var(--green);border-radius:3px;display:flex;align-items:center;justify-content:center">
    <svg width="14" height="9" viewBox="0 0 14 9"><path d="M1 8l6-6 6 6" fill="#fff"/></svg></div>
  <div class="abs" style="left:84px;top:4497px;width:1032px;height:1px;background:#2a3560"></div>

  <h2 class="abs" style="left:0;width:1200px;top:4560px;text-align:center;color:#fff;font-size:27px;font-weight:700">Get free assessment today</h2>
  <p class="abs" style="left:300px;width:600px;top:4610px;text-align:center;color:#fff;font-size:14px;line-height:24px">Lorem ipsum dolor sit amet, consectetur adipiscing elit, sed do eiusmod tempor incididunt ut labore et dolore magna aliqua.</p>

  <div class="abs contact-item" style="left:220px;top:4698px">
    <svg width="46" height="46" viewBox="0 0 24 24" fill="none" stroke="#4a8f2c" stroke-width="1.3"><path d="M22 16.9v3a2 2 0 0 1-2.2 2 19.8 19.8 0 0 1-8.6-3.1 19.5 19.5 0 0 1-6-6A19.8 19.8 0 0 1 2.1 4.2 2 2 0 0 1 4.1 2h3a2 2 0 0 1 2 1.7c.1.9.4 1.8.7 2.7a2 2 0 0 1-.5 2.1L8 9.8a16 16 0 0 0 6 6l1.3-1.3a2 2 0 0 1 2.1-.4c.9.3 1.8.6 2.7.7a2 2 0 0 1 1.7 2z"/></svg>
    <div><div class="lbl">Make a Call</div><div class="val">+1-868-555-0187</div></div></div>
  <div class="abs" style="left:440px;top:4695px;width:1px;height:56px;background:#2a3560"></div>
  <div class="abs contact-item" style="left:474px;top:4698px">
    <svg width="46" height="46" viewBox="0 0 24 24" fill="none" stroke="#4a8f2c" stroke-width="1.3"><rect x="2" y="5" width="20" height="15" rx="1"/><path d="M2 6l10 7 10-7M2 20l7-7M22 20l-7-7"/></svg>
    <div><div class="lbl">Mail Us On</div><div class="val">info@torvane.example</div></div></div>
  <div class="abs" style="left:726px;top:4695px;width:1px;height:56px;background:#2a3560"></div>
  <div class="abs contact-item" style="left:756px;top:4698px">
    <svg width="46" height="46" viewBox="0 0 24 24" fill="none" stroke="#4a8f2c" stroke-width="1.3"><path d="M12 17s-5-4.5-5-8.5a5 5 0 0 1 10 0c0 4-5 8.5-5 8.5z"/><circle cx="12" cy="8.5" r="1.8"/><path d="M6 15l-4 7h20l-4-7"/></svg>
    <div><div class="lbl">Location</div><div class="val">18 Shore Road, Tobago</div></div></div>

  <div class="abs bottom-bar">
    <div class="abs" style="left:84px;top:20px">Torvane Health</div>
    <div class="abs" style="left:800px;top:20px;display:flex;gap:20px"><a>Privacy Policy</a><a>Terms &amp; Conditions</a><a>Site Map</a></div>
  </div>
</footer>

</div>
</body>
</html>
```